Dietitian clinic needs a business card design

We need a business card design for a new dietitian group based in Singapore called "Lantern and Tide". We provide expert, personalised nutrition care to support a wide range of health needs, from chronic conditions to mindful eating. Our team also offers consulting, speaking, and tailored solutions for healthcare providers, organisations, and food services.

Target Market(s)

Adults

Industry/Entity Type

Healthcare

Contact Information for Business Card

Name, position, contact number, email, website address, our logo

Requirements
Nice to have
• Clean, professional but welcoming look

```html
<!DOCTYPE html>
<html lang="en">
<head>
<meta charset="utf-8">
<title>Lantern and Tide – Business Card</title>
<link rel="stylesheet" href="https://fonts.googleapis.com/css2?family=Lato:wght@400;700;900&display=swap">
<style>
  :root {
    --teal: #245a6b;
    --white: #ffffff;
    --ink: #1c1c1c;
    --rule: #2a2a2a;
    --stage: #2b2b2d;
  }
  * { box-sizing: border-box; margin: 0; padding: 0; }
  html, body { width: 1200px; height: 880px; overflow: hidden; }
  body {
    background: var(--stage);
    font-family: "Lato", Arial, sans-serif;
    position: relative;
  }
  .card {
    position: absolute;
    left: 270px;
    width: 660px;
    height: 377px;
    border-radius: 26px;
    overflow: hidden;
  }
  .card--front { top: 42px; background: var(--teal); }
  .card--back { top: 461px; background: var(--white); }

  .brand {
    position: absolute;
    display: flex;
    align-items: center;
    gap: 18px;
    font-weight: 900;
    letter-spacing: 0.5px;
    line-height: 1;
    white-space: nowrap;
  }
  .brand__dot { border-radius: 50%; flex: none; }
  .card--front .brand { left: 50%; top: 50%; transform: translate(-50%, -50%); color: var(--white); font-size: 52px; }
  .card--front .brand__dot { width: 46px; height: 46px; background: var(--white); }
  .card--back .brand { left: 225px; top: 60px; color: var(--teal); font-size: 32px; gap: 12px; }
  .card--back .brand__dot { width: 28px; height: 28px; background: var(--teal); }

  .rule-long {
    position: absolute;
    left: 200px; right: 40px; top: 140px;
    height: 1.5px; background: var(--rule);
  }
  .person { position: absolute; left: 40px; top: 190px; }
  .person__name { color: var(--teal); font-size: 27px; font-weight: 700; letter-spacing: 0.3px; }
  .person__role { color: var(--ink); font-size: 17px; margin-top: 4px; }
  .rule-short {
    position: absolute; left: 40px; top: 262px;
    width: 190px; height: 1.5px; background: var(--rule);
  }
  .contacts { position: absolute; left: 40px; top: 276px; list-style: none; }
  .contacts li { display: flex; align-items: center; gap: 12px; font-size: 17px; color: var(--ink); height: 26px; }
  .contacts svg { width: 16px; height: 16px; fill: var(--teal); flex: none; }
  .address {
    position: absolute; right: 40px; top: 180px;
    text-align: right; font-size: 16px; color: var(--ink); line-height: 1.45;
  }
  .band { position: absolute; left: 0; bottom: 0; width: 660px; height: 80px; }
  .website {
    position: absolute; right: 40px; bottom: 24px;
    color: var(--white); font-size: 16px; letter-spacing: 0.3px;
  }
</style>
</head>
<body>
  <section class="card card--front" aria-label="Card front">
    <div class="brand"><span class="brand__dot"></span>lantern &amp; tide</div>
  </section>

  <section class="card card--back" aria-label="Card back">
    <div class="brand"><span class="brand__dot"></span>lantern &amp; tide</div>
    <div class="rule-long"></div>

    <div class="person">
      <p class="person__name">MARCUS HALE</p>
      <p class="person__role">Managing Director</p>
    </div>
    <div class="rule-short"></div>
    <ul class="contacts">
      <li>
        <svg viewBox="0 0 24 24" aria-hidden="true"><path d="M6.6 10.8a15.1 15.1 0 0 0 6.6 6.6l2.2-2.2a1 1 0 0 1 1-.25 11.4 11.4 0 0 0 3.6.57 1 1 0 0 1 1 1V20a1 1 0 0 1-1 1A17 17 0 0 1 3 4a1 1 0 0 1 1-1h3.5a1 1 0 0 1 1 1c0 1.25.2 2.45.57 3.57a1 1 0 0 1-.25 1z"/></svg>
        065-321 908 447
      </li>
      <li>
        <svg viewBox="0 0 24 24" aria-hidden="true"><path d="M2 5h20v14H2z M2 5l10 8 10-8" fill="none" stroke="#245a6b" stroke-width="0"/><path d="M2 6.5V19h20V6.5l-10 7.5z M3 5h18l-9 6.8z"/></svg>
        hello@lanterntide.sg
      </li>
    </ul>

    <p class="address">18 Tanjong Pagar Road<br>088441, Singapore</p>

    <svg class="band" viewBox="0 0 660 80" preserveAspectRatio="none" aria-hidden="true">
      <path d="M0 68 L360 52 L360 58 L0 74 Z" fill="#245a6b"/>
      <path d="M0 78 L368 62 L378 38 L660 22 L660 80 L0 80 Z" fill="#245a6b"/>
    </svg>
    <p class="website">www.lanterntide.sg</p>
  </section>
</body>
</html>
```